A business selling natural soaps online and in farmers markets. I want it to reflect local commerce and natural lifestyle. My colors are olive green and saddle brown. I want the dimensions to be 2.25 x 3.25" with matte finish.

The name of my company is Fernwick Soapery, LLC

Business

```html
<!DOCTYPE html>
<html lang="en">
<head>
<meta charset="utf-8">
<title>Fernwick Soapery, LLC — Business Card</title>
<link rel="stylesheet" href="https://fonts.googleapis.com/css2?family=Open+Sans:wght@400&family=Tinos:wght@700&display=swap">
<style>
  :root {
    --card-green: #a3c27a;
    --leaf-light: #b2cf8a;
    --leaf-mid: #8db35c;
    --leaf-deep: #6f9a3c;
    --saddle-brown: #8b4513;
    --ink: #111111;
    --paper: #ffffff;
  }
  html, body {
    margin: 0;
    padding: 0;
    width: 1200px;
    height: 839px;
    overflow: hidden;
  }
  .card {
    position: relative;
    width: 1200px;
    height: 839px;
    overflow: hidden;
    background: var(--card-green);
    font-family: "Open Sans", Arial, sans-serif;
    color: var(--ink);
  }
  .card__texture {
    position: absolute;
    inset: 0;
    background:
      linear-gradient(90deg,
        var(--leaf-light) 0%,
        var(--leaf-mid) 12%,
        var(--card-green) 22%,
        var(--leaf-deep) 34%,
        var(--card-green) 46%,
        var(--leaf-mid) 58%,
        var(--card-green) 70%,
        var(--leaf-mid) 82%,
        var(--leaf-light) 100%);
    opacity: 0.75;
  }
  .brand-mark {
    position: absolute;
    left: 68px;
    top: 52px;
    width: 289px;
    height: 360px;
    display: flex;
    flex-direction: column;
    align-items: center;
    justify-content: center;
    gap: 26px;
  }
  .brand-mark__square {
    width: 170px;
    height: 170px;
    background: var(--saddle-brown);
  }
  .brand-mark__name {
    color: var(--saddle-brown);
    font-size: 60px;
    line-height: 1;
  }
  .website {
    position: absolute;
    left: 384px;
    top: 146px;
    margin: 0;
    font-size: 90px;
    line-height: 1;
    letter-spacing: -1px;
  }
  .contact {
    position: absolute;
    right: 66px;
    top: 322px;
    margin: 0;
    text-align: right;
    font-family: "Tinos", "Times New Roman", serif;
    font-weight: 700;
    font-size: 37px;
    line-height: 53px;
  }
  .contact span {
    display: block;
    text-decoration: underline;
    text-decoration-thickness: 2px;
    text-underline-offset: 5px;
  }
  .company-name {
    position: absolute;
    left: 0;
    width: 1190px;
    top: 435px;
    margin: 0;
    text-align: center;
    color: var(--paper);
    font-weight: 400;
    font-size: 98px;
    line-height: 1;
    letter-spacing: -0.5px;
  }
  .divider {
    position: absolute;
    left: 583px;
    top: 550px;
    width: 2px;
    height: 240px;
    background: var(--ink);
  }
  .market {
    position: absolute;
    top: 541px;
  }
  .market--left {
    right: 634px;
    text-align: right;
  }
  .market--right {
    left: 602px;
    text-align: left;
  }
  .market__title {
    margin: 0 0 6px;
    padding-bottom: 2px;
    border-bottom: 2px solid var(--ink);
    font-family: "Tinos", "Times New Roman", serif;
    font-weight: 700;
    font-size: 35px;
    line-height: 42px;
    white-space: nowrap;
  }
  .market--left .market__title { padding-left: 4px; }
  .market--right .market__title { padding-right: 4px; }
  .market__details {
    margin: 0;
    font-size: 35px;
    line-height: 53px;
    white-space: nowrap;
  }
  .market__details span { display: block; }
</style>
</head>
<body>
  <main class="card">
    <div class="card__texture" role="img" aria-label="Soft painted green brushstroke background texture"></div>

    <div class="brand-mark">
      <span class="brand-mark__square"></span>
      <span class="brand-mark__name">Fernwick</span>
    </div>

    <p class="website">fernwicksoap.com</p>

    <p class="contact">
      <span>info@fernwicksoap.com</span>
      <span>Dunmore, Virginia 22140</span>
    </p>

    <h1 class="company-name">Fernwick Soapery, LLC</h1>

    <section class="market market--left">
      <h2 class="market__title">Elm Hollow Farmers Market</h2>
      <p class="market__details">
        <span>Saturdays 8 am -12 pm</span>
        <span>Town Hall Parking Lot</span>
        <span>410 Birch Avenue</span>
        <span>Elm Hollow, Virginia</span>
      </p>
    </section>

    <div class="divider"></div>

    <section class="market market--right">
      <h2 class="market__title">Cedar Ridge Farmers Market</h2>
      <p class="market__details">
        <span>Sundays 9:00 am – 1:00 pm</span>
        <span>Cedar Ridge Road and Mill</span>
        <span>Creek Drive</span>
        <span>Alder Springs, Virginia</span>
      </p>
    </section>
  </main>
</body>
</html>
```